New Business and Accounting Software need a Web Site

The website is for a Business and Accounting Software that has 8 products.
Each product has its owns logo and color, when you do the design have in consideration that we are looking the experience that when you change from one product page to another the look and feel adjust to the color and logo of the product.
The product are:
Ventas (Sales)
Compras (Purchases)
Contabilidad (Accounting)
Presupuesto (Budget)
Inventarios (Inventory)
Bancos (Banks)
NĂ³mina RH (Human Resources Payroll)
CRM (Customer Relationship Manager)

You can see how the main logo and variations are used in each page
- https://www.ufta.com/
- https://www.vemi.com/
- https://www.prulvin.com/

Our goal is to be similar to them.

I have created a word document to explain what I want.
You need to design:
1 Home Page
1 Product Landing Page
1 Product Detail Page
1 Price Page

I am attaching:
1. Main Logo
2. 8 Product Logos
3. Website Idea, you can create your own idea.

You are welcome to use other icons for the each product if you want.

Target Market(s)

Independet professionals and Small and Medium Companies

Industry/Entity Type

Business and Accounting Software

Coding

Coded - Design and coding required

Colors
0054AA
0677BA
7BADD7
CADEEF
E8F1F8

Requirements
Must have
• Must show all products in the main page

```html
<!DOCTYPE html>
<html lang="en">
<head>
<meta charset="utf-8">
<title>Tarva — All in one Software</title>
<link href="https://fonts.googleapis.com/css2?family=Kumbh+Sans:wght@500;600;700&family=Poppins:wght@400;500;600&display=swap" rel="stylesheet">
<style>
:root{
  --blue:#0054AA;
  --blue-mid:#0677BA;
  --blue-soft:#7BADD7;
  --blue-pale:#CADEEF;
  --blue-mist:#E8F1F8;
  --steel:#6597C6;
  --ink:#1d1d1f;
  --text:#4a4a4a;
  --white:#fff;
}
*{box-sizing:border-box;margin:0;padding:0}
html,body{width:1200px;height:4412px;overflow:hidden}
body{position:relative;background:var(--white);font-family:"Poppins",sans-serif;color:var(--text)}
.abs{position:absolute}
h1,h2,h3,.heading{font-family:"Kumbh Sans",sans-serif}

/* brand */
.brand{display:flex;align-items:center;gap:10px;text-decoration:none}
.brand-dot{width:56px;height:56px;border-radius:50%;background:var(--blue-mid)}
.brand-name{font-family:"Kumbh Sans",sans-serif;font-weight:700;font-size:44px;color:var(--blue);letter-spacing:-.5px}

/* nav */
.topbar{left:0;top:0;width:1200px;height:92px;background:var(--white)}
.topbar .brand{position:absolute;left:92px;top:18px}
.nav-links{position:absolute;top:34px;left:0;width:100%;font-size:16px;color:var(--ink)}
.nav-links a{position:absolute;text-decoration:none;color:var(--ink)}
.nav-links a.active{color:var(--blue)}
.btn{display:flex;align-items:center;justify-content:center;border-radius:24px;font-size:16px;font-weight:500;color:var(--white);text-decoration:none}
.btn-signin{left:842px;top:27px;width:117px;height:41px;background:var(--blue)}
.btn-trial-nav{left:971px;top:27px;width:135px;height:41px;background:var(--blue-soft)}

/* hero */
.hero{left:0;top:92px;width:1200px;height:576px;background:linear-gradient(120deg,#0a3d8f 0%,var(--blue) 55%,#0b48a8 100%);clip-path:polygon(0 0,100% 0,100% 82%,0 100%)}
.hero-kicker{left:92px;top:230px;font-size:22px;letter-spacing:4px;color:var(--white);font-weight:500}
.hero-title{left:92px;top:262px;font-size:54px;line-height:62px;font-weight:700;color:var(--white)}
.hero-title span{color:var(--blue-soft)}
.btn-hero{left:92px;top:426px;width:180px;height:50px;border:2px solid var(--blue-soft);background:transparent;font-size:18px}
.hero-visual{left:497px;top:171px;width:607px;height:343px;border-radius:14px;background:linear-gradient(135deg,#1c3fae,#2a5fd1 60%,#1632a0)}

/* apps */
.apps-title{left:0;top:733px;width:1200px;text-align:center;font-size:40px;font-weight:700;color:var(--ink)}
.apps-title span{color:var(--blue-mid)}
.app-card{width:226px;height:75px;border:2px solid;border-radius:6px;display:flex;flex-direction:column;align-items:center;justify-content:center;background:var(--white)}
.app-card .app-name{font-family:"Kumbh Sans",sans-serif;font-weight:700;font-size:28px;line-height:28px;color:var(--blue)}
.app-card .app-product{font-size:9px;letter-spacing:3px;text-transform:uppercase;color:var(--text);margin-top:3px}

/* perfil */
.perfil{left:0;top:1138px;width:1200px;height:1190px;background:var(--steel);clip-path:polygon(0 43px,100% 0,100% 100%,0 100%)}
.perfil-title{left:0;top:1222px;width:1200px;text-align:center;font-size:36px;font-weight:700;color:var(--white)}
.hex{clip-path:polygon(25% 0,75% 0,100% 50%,75% 100%,25% 100%,0 50%);background:var(--white);text-align:center;padding-top:52px}
.hex h3{font-size:23px;font-weight:700;color:var(--ink)}
.hex h3::after{content:"";display:block;width:30px;height:3px;background:var(--blue-mid);margin:6px auto 0;border-radius:2px}
.hex p{font-size:15.5px;line-height:28px;color:var(--text);width:260px;margin:12px auto 0}
.hex a{display:inline-flex;align-items:center;gap:8px;margin-top:14px;font-size:15.5px;color:var(--blue-mid);text-decoration:none;font-weight:500}
.hex-photo{background:linear-gradient(180deg,var(--blue-mist),var(--blue-pale))}
.deco-hex{clip-path:polygon(25% 0,75% 0,100% 50%,75% 100%,25% 100%,0 50%)}
.person{left:388px;top:1710px;width:420px;height:540px;border-radius:200px 200px 60px 60px;background:linear-gradient(180deg,#c79a7d 0%,#8b3f3a 35%,#3a4a6b 70%,#2b3550 100%)}

/* tabs */
.tabs{left:199px;top:2410px;width:803px;height:90px;background:var(--white);box-shadow:0 6px 24px rgba(0,40,90,.12);border-radius:4px;display:flex;align-items:center}
.tab{display:flex;flex-direction:column;align-items:center;justify-content:center;gap:8px;height:90px;font-size:15px;color:var(--ink)}
.tab.active{background:var(--blue);color:var(--white);border-radius:4px}
.tab-arrow{top:2442px;color:var(--blue-soft)}

/* balance */
.shot{left:94px;top:2611px;width:569px;height:380px;border-radius:6px;background:var(--white);box-shadow:0 8px 30px rgba(0,40,90,.18);border-bottom:4px solid var(--blue);overflow:hidden}
.shot-bar{height:24px;background:#f0f2f5}
.shot-menu{height:12px;background:var(--blue)}
.shot-body{position:absolute;left:14px;right:14px;top:60px;bottom:14px;background:linear-gradient(180deg,var(--blue-mist),#f7f9fc)}
.balance-title{left:726px;top:2674px;font-size:38px;font-weight:700;color:var(--ink)}
.balance-title span{color:var(--blue-mid)}
.balance-copy{left:726px;top:2744px;width:384px;font-size:16px;line-height:28px;color:var(--text)}

/* features */
.feature{top:3164px;width:235px;height:298px;border:2px solid var(--blue);border-top:0;border-radius:20px 0 60px 0;padding:42px 26px 0;background:var(--white)}
.feature.active{background:var(--blue);color:var(--white)}
.feature h3{font-size:18px;font-weight:700;color:var(--ink);margin-top:18px}
.feature.active h3{color:var(--white)}
.feature h3::after{content:"";display:block;width:26px;height:2px;background:var(--blue-soft);margin:10px 0 0 20px}
.feature p{font-size:15.5px;line-height:28px;margin-top:12px}
.feature svg{display:block}

/* cta */
.cta{left:0;top:3544px;width:1200px;height:496px;background:linear-gradient(120deg,#0a4da3,var(--blue) 50%,#0a5bb8);clip-path:polygon(0 38px,100% 0,100% 100%,0 100%)}
.cta-kicker{left:92px;top:3684px;font-size:20px;color:var(--white)}
.cta-title{left:92px;top:3724px;font-size:38px;line-height:50px;font-weight:700;color:var(--white)}
.btn-cta{left:92px;top:3849px;width:276px;height:51px;background:var(--blue-soft);font-size:18px}
.cta-frame{left:604px;top:3636px;width:503px;height:339px;border-radius:26px;border:3px solid var(--blue-soft)}
.cta-visual{left:594px;top:3624px;width:503px;height:339px;border-radius:26px;background:linear-gradient(135deg,#5a4a3a,#c8a058 45%,#8a6a4a)}

/* footer */
.footer-brand{left:92px;top:4103px}
.social{top:4189px;width:48px;height:48px;border-radius:50%;background:var(--blue)}
.foot-col h4{font-family:"Kumbh Sans",sans-serif;font-size:19px;font-weight:700;color:var(--ink);margin-bottom:18px}
.foot-col li{list-style:none;font-size:15px;color:var(--ink);margin-bottom:14px}
.contact-item{display:flex;gap:14px;font-size:15px;color:var(--ink);line-height:21px;margin-bottom:14px}
.contact-item svg{flex:none;margin-top:2px}
.news-input{left:825px;top:4144px;width:281px;height:47px;border-radius:24px;background:#e9ecf1;font-size:15px;color:var(--ink);padding:14px 20px}
.news-btn{left:825px;top:4206px;width:281px;height:47px;background:var(--blue);font-size:17px;font-weight:600}
.footer-rule{left:0;top:4348px;width:1200px;height:1px;background:#dde3ea}
.copyright{left:0;top:4367px;width:1200px;text-align:center;font-size:14px;color:var(--text)}
</style>
</head>
<body>

<!-- navigation -->
<header class="abs topbar">
  <a class="brand" href="#"><span class="brand-dot"></span><span class="brand-name">tarva</span></a>
  <nav class="nav-links">
    <a class="active" style="left:404px">Home</a>
    <a style="left:493px">Soluciones</a>
    <a style="left:620px">Prices</a>
    <a style="left:709px">Contact Us</a>
  </nav>
  <a class="abs btn btn-signin" href="#">Sign In</a>
  <a class="abs btn btn-trial-nav" href="#">Free Trial</a>
</header>

<!-- hero -->
<section class="abs hero"></section>
<p class="abs hero-kicker">All in one Software</p>
<h1 class="abs hero-title">Platform to run<br>your <span>business.</span></h1>
<a class="abs btn btn-hero" href="#">Free Trial</a>
<div class="abs hero-visual" role="img" aria-label="Laptop showing the software's start screen on a blue wave background"></div>

<!-- featured apps -->
<h2 class="abs apps-title">Featured <span>apps</span></h2>
<div class="abs app-card" style="left:122px;top:827px;border-color:#f0a35a"><span class="app-name">tarva</span><span class="app-product">Ventas</span></div>
<div class="abs app-card" style="left:365px;top:827px;border-color:#6fa5dc"><span class="app-name">tarva</span><span class="app-product">Compras</span></div>
<div class="abs app-card" style="left:608px;top:827px;border-color:#d98ac8"><span class="app-name">tarva</span><span class="app-product">Contabilidad</span></div>
<div class="abs app-card" style="left:853px;top:827px;border-color:#e0575f"><span class="app-name">tarva</span><span class="app-product">Inventarios</span></div>
<div class="abs app-card" style="left:122px;top:938px;border-color:#707070"><span class="app-name">tarva</span><span class="app-product">Bancos</span></div>
<div class="abs app-card" style="left:365px;top:938px;border-color:#2fb28a"><span class="app-name">tarva</span><span class="app-product">Presupuesto</span></div>
<div class="abs app-card" style="left:608px;top:938px;border-color:#77c7b4"><span class="app-name">tarva</span><span class="app-product">Nómina RH</span></div>
<div class="abs app-card" style="left:853px;top:938px;border-color:#7a6ad8"><span class="app-name">tarva</span><span class="app-product">CRM</span></div>

<!-- perfil -->
<section class="abs perfil"></section>
<h2 class="abs perfil-title">Is it to perfil?</h2>
<div class="abs deco-hex" style="left:94px;top:1390px;width:42px;height:38px;background:#8fb4d8"></div>
<div class="abs deco-hex" style="left:132px;top:1408px;width:68px;height:60px;background:var(--white)"></div>
<div class="abs deco-hex" style="left:918px;top:1390px;width:42px;height:38px;background:var(--white)"></div>
<div class="abs deco-hex" style="left:956px;top:1408px;width:68px;height:60px;background:#8fb4d8"></div>

<div class="abs hex hex-photo" style="left:409px;top:1770px;width:380px;height:328px"></div>
<div class="abs person" role="img" aria-label="Smiling young man in a checked shirt sitting cross-legged with a laptop"></div>

<article class="abs hex" style="left:409px;top:1325px;width:380px;height:328px">
  <h3>Profesional</h3>
  <p>Lorem ipsum dolor sit amet sed consectetur adipisicing elit sed do eiusmod tempor incididunt ut labore et dolore magna aliqua.Ut enim ad minim veniam quis nostrud exercitation</p>
  <a href="#">More Information <svg width="14" height="12" viewBox="0 0 14 12"><path d="M1 6h11M7 1l5 5-5 5" fill="none" stroke="currentColor" stroke-width="2"/></svg></a>
</article>
<article class="abs hex" style="left:94px;top:1500px;width:380px;height:328px">
  <h3>Contador</h3>
  <p>Lorem ipsum dolor sit amet sed consectetur adipisicing elit sed do eiusmod tempor incididunt ut labore et dolore magna aliqua.Ut enim ad minim veniam quis nostrud exercitation</p>
  <a href="#">More Information <svg width="14" height="12" viewBox="0 0 14 12"><path d="M1 6h11M7 1l5 5-5 5" fill="none" stroke="currentColor" stroke-width="2"/></svg></a>
</article>
<article class="abs hex" style="left:724px;top:1500px;width:380px;height:328px">
  <h3>PYME</h3>
  <p>Lorem ipsum dolor sit amet sed consectetur adipisicing elit sed do eiusmod tempor incididunt ut labore et dolore magna aliqua.Ut enim ad minim veniam quis nostrud exercitation</p>
  <a href="#">More Information <svg width="14" height="12" viewBox="0 0 14 12"><path d="M1 6h11M7 1l5 5-5 5" fill="none" stroke="currentColor" stroke-width="2"/></svg></a>
</article>
<article class="abs hex" style="left:94px;top:1856px;width:380px;height:328px">
  <h3>Micro</h3>
  <p>Lorem ipsum dolor sit amet sed consectetur adipisicing elit sed do eiusmod tempor incididunt ut labore et dolore magna aliqua.Ut enim ad minim veniam quis nostrud exercitation</p>
  <a href="#">More Information <svg width="14" height="12" viewBox="0 0 14 12"><path d="M1 6h11M7 1l5 5-5 5" fill="none" stroke="currentColor" stroke-width="2"/></svg></a>
</article>
<article class="abs hex" style="left:724px;top:1856px;width:380px;height:328px">
  <h3>Empresarial</h3>
  <p>Lorem ipsum dolor sit amet sed consectetur adipisicing elit sed do eiusmod tempor incididunt ut labore et dolore magna aliqua.Ut enim ad minim veniam quis nostrud exercitation</p>
  <a href="#">More Information <svg width="14" height="12" viewBox="0 0 14 12"><path d="M1 6h11M7 1l5 5-5 5" fill="none" stroke="currentColor" stroke-width="2"/></svg></a>
</article>

<!-- module tabs -->
<svg class="abs tab-arrow" style="left:146px" width="22" height="16" viewBox="0 0 22 16"><path d="M21 8H2M8 1L1 8l7 7" fill="none" stroke="currentColor" stroke-width="2"/></svg>
<nav class="abs tabs">
  <div class="tab active" style="width:148px">
    <svg width="16" height="20" viewBox="0 0 16 20"><path d="M0 0h11l5 5v15H0z" fill="currentColor"/><path d="M4 10h8M4 14h8" stroke="#0054AA" stroke-width="2"/></svg>Balance Sheet</div>
  <div class="tab" style="width:185px">
    <svg width="20" height="20" viewBox="0 0 20 20"><path d="M10 1l9 5H1z M2 8h3v8H2z M8.5 8h3v8h-3z M15 8h3v8h-3z M1 17h18v3H1z" fill="currentColor"/></svg>Banks</div>
  <div class="tab" style="width:75px">
    <svg width="16" height="20" viewBox="0 0 16 20"><path d="M0 0h16v20l-4-3-4 3-4-3-4 3z" fill="currentColor"/><path d="M4 6h8M4 10h8" stroke="#fff" stroke-width="2"/></svg>Bills</div>
  <div class="tab" style="width:220px">
    <svg width="20" height="20" viewBox="0 0 20 20"><path d="M9 2a9 9 0 1 0 9 9H9z" fill="currentColor"/><path d="M11 0v9h9a9 9 0 0 0-9-9z" fill="currentColor"/></svg>Chat of Account</div>
  <div class="tab" style="width:175px">
    <svg width="18" height="20" viewBox="0 0 18 20"><path d="M0 0h11v20H0z" fill="currentColor"/><path d="M12 10h6M15 7l3 3-3 3" fill="none" stroke="currentColor" stroke-width="2"/></svg>CheckOut</div>
</nav>
<svg class="abs tab-arrow" style="left:1033px" width="22" height="16" viewBox="0 0 22 16"><path d="M1 8h19M14 1l7 7-7 7" fill="none" stroke="currentColor" stroke-width="2"/></svg>

<!-- balance sheet -->
<div class="abs shot" role="img" aria-label="Software window showing a trial balance report table">
  <div class="shot-bar"></div>
  <div class="shot-menu"></div>
  <div class="shot-body"></div>
</div>
<h2 class="abs balance-title">Balance <span>sheet</span></h2>
<p class="abs balance-copy">Lorem ipsum dolor sit amet consectetur cingy adipisicingy elit sed do eiusmod tempor utter incididunt ut labore etoi dolore magna aliqua. Ut enim ad minim veniam, quiso nostrud office exercitation ullamco laboris nisi ut aliquip exi ea commodo consequat. Duis aute irure dolor in your reprehenderit in voluptate velit.</p>

<!-- features -->
<article class="abs feature" style="left:94px">
  <svg width="58" height="58" viewBox="0 0 58 58" fill="none" stroke="#0677BA" stroke-width="2"><rect x="2" y="14" width="54" height="40" rx="3"/><path d="M29 4c7 6 9 16 6 28H23c-3-12-1-22 6-28z"/><circle cx="29" cy="18" r="3"/><path d="M23 32l-5 6 5-1M35 32l5 6-5-1M26 36l3 8 3-8"/></svg>
  <h3>Page Por Uso</h3>
  <p>Page solo por las funcionalidades que te interesan</p>
</article>
<article class="abs feature active" style="left:353px">
  <svg width="58" height="58" viewBox="0 0 58 58" fill="none" stroke="#fff" stroke-width="2"><path d="M4 2h34v54H4z"/><path d="M10 12h22M10 20h22M10 28h14"/><circle cx="14" cy="44" r="6"/><path d="M28 48l24-30 4 3-24 30-6 2z"/></svg>
  <h3>Sin Contrato</h3>
  <p>Page solo por las funcionalidades que te interesan</p>
</article>
<article class="abs feature" style="left:611px">
  <svg width="62" height="58" viewBox="0 0 62 58" fill="none" stroke="#0677BA" stroke-width="2"><path d="M14 44a10 10 0 0 1 0-20 16 16 0 0 1 31-4 12 12 0 0 1 4 24z"/></svg>
  <h3>En La Nube</h3>
  <p>Page solo por las funcionalidades que te interesan</p>
</article>
<article class="abs feature" style="left:870px">
  <svg width="66" height="58" viewBox="0 0 66 58" fill="none" stroke="#0677BA" stroke-width="2"><rect x="2" y="8" width="40" height="30" rx="2"/><path d="M14 46h16M22 38v8"/><rect x="38" y="24" width="16" height="28" rx="2"/><rect x="54" y="30" width="10" height="18" rx="2"/></svg>
  <h3>Multiples Dispositivos</h3>
  <p>Page solo por las funcionalidades que te interesan</p>
</article>

<!-- call to action -->
<section class="abs cta"></section>
<p class="abs cta-kicker">What are you waiting for</p>
<h2 class="abs cta-title">To create one free<br>account In Tarva?</h2>
<a class="abs btn btn-cta" href="#">Crear Cuenta Gratis</a>
<div class="abs cta-frame"></div>
<div class="abs cta-visual" role="img" aria-label="Person in a yellow sweater typing on a laptop at a wooden desk"></div>

<!-- footer -->
<a class="abs brand footer-brand" href="#"><span class="brand-dot"></span><span class="brand-name">tarva</span></a>
<span class="abs social" style="left:92px" aria-label="Social profile 1"></span>
<span class="abs social" style="left:149px" aria-label="Social profile 2"></span>
<span class="abs social" style="left:205px" aria-label="Social profile 3"></span>

<div class="abs foot-col" style="left:360px;top:4098px">
  <h4>Quick Links</h4>
  <ul><li>Home</li><li>Soluciones</li><li>Prices</li><li>Contact Us</li></ul>
</div>
<div class="abs foot-col" style="left:551px;top:4098px;width:230px">
  <h4>Contact info</h4>
  <div class="contact-item"><svg width="18" height="20" viewBox="0 0 18 20" fill="none" stroke="#0054AA" stroke-width="2"><path d="M9 19s7-7 7-11A7 7 0 0 0 2 8c0 4 7 11 7 11z"/><circle cx="9" cy="8" r="2.5"/></svg><span>tempor inci incidi ut<br>labore et dolore</span></div>
  <div class="contact-item"><svg width="18" height="18" viewBox="0 0 18 18" fill="none" stroke="#0054AA" stroke-width="2"><path d="M4 1l3 4-2 2a11 11 0 0 0 6 6l2-2 4 3-2 3C8 17 1 10 1 4z"/></svg><span>555-014-2290</span></div>
  <div class="contact-item"><svg width="20" height="16" viewBox="0 0 20 16" fill="none" stroke="#0054AA" stroke-width="2"><rect x="1" y="1" width="18" height="14"/><path d="M1 1l9 8 9-8"/></svg><span>hola@tarva.com</span></div>
</div>
<div class="abs foot-col" style="left:823px;top:4098px"><h4>Newsletter</h4></div>
<div class="abs news-input">Email Address..</div>
<a class="abs btn news-btn" href="#">Subscribe !</a>

<div class="abs footer-rule"></div>
<p class="abs copyright">© 2022 Tarva. All Rights Reserved</p>

</body>
</html>
```